Poster for List of Company Values

We need a poster to outline our Values which will be displayed in our office as well as posted on our website and other platforms (so need to allow for some flexibly in its application).

File attached outlines what we currently have with design and also our company style guide.

Note that we are looking for a modern, clean look, which still represents our core activities of construction and environmental services.

You can also reference our website here:

https://quorvelgroup.com.au/

Happy to answer any questions you might have.

Thanks for your interest,
Brent

Target Market(s)

Internal and External clients

Industry/Entity Type

Construction, water and recycling

Font styles to use
Sans Serif

Requirements
Must have
• All values on the one page. Graphic to represent each value. Also needs to use company logo
Nice to have
• Preference for poster to be orientated in landscape
Should not have
• Do not follow example provided, this is only to demonstrate what we have to date and also the text required

```html
<!DOCTYPE html>
<html lang="en">
<head>
<meta charset="utf-8">
<title>Core Values – Quorvel Group</title>
<link href="https://fonts.googleapis.com/css2?family=Carlito:wght@400;700&display=swap" rel="stylesheet">
<style>
  :root {
    --navy: #0a3f8a;
    --green: #4bae4a;
    --paper: #dfdfdf;
    --white: #ffffff;
    --ink: #3b3b3b;
  }
  * { box-sizing: border-box; margin: 0; padding: 0; }
  html, body { width: 1200px; height: 849px; overflow: hidden; }
  body {
    position: relative;
    background: var(--paper);
    font-family: "Carlito", "Calibri", sans-serif;
  }
  .poster-title {
    position: absolute;
    top: 42px; left: 0; width: 1200px;
    text-align: center;
    color: var(--navy);
    font-size: 56px;
    font-weight: 700;
    letter-spacing: 1px;
    word-spacing: 12px;
  }
  .value-card {
    position: absolute;
    width: 323px; height: 267px;
    background: var(--navy);
    border-radius: 39px;
    color: var(--white);
    padding: 52px 20px 0 24px;
  }
  .value-card .notch {
    position: absolute;
    left: 228px; top: -18px;
    width: 114px; height: 114px;
    border-radius: 50%;
    background: var(--paper);
  }
  .value-card .badge {
    position: absolute;
    left: 242px; top: -4px;
    width: 86px; height: 86px;
    border-radius: 50%;
    background: var(--green);
  }
  .value-card .badge-icon {
    position: absolute;
    left: 14px; top: 14px;
    width: 58px; height: 58px;
    border-radius: 50%;
    background: var(--white);
  }
  .value-name {
    position: relative;
    font-size: 21.5px;
    font-weight: 700;
    line-height: 28px;
    max-width: 160px;
  }
  .value-text {
    position: relative;
    margin-top: 28px;
    font-size: 21.5px;
    font-weight: 700;
    line-height: 28px;
    text-align: justify;
    hyphens: none;
  }
  .col-1 { left: 78px; }
  .col-2 { left: 438px; }
  .col-3 { left: 799px; }
  .row-1 { top: 134px; }
  .row-2 { top: 434px; }
  .footer {
    position: absolute;
    left: 0; top: 730px;
    width: 1200px; height: 119px;
    background: var(--white);
  }
  .brand {
    position: absolute;
    left: 412px; top: 38px;
    display: flex; align-items: center; gap: 12px;
  }
  .brand-mark {
    width: 52px; height: 52px;
    background: var(--navy);
  }
  .brand-name {
    color: var(--ink);
    font-size: 23px;
    font-weight: 700;
    line-height: 21px;
  }
  .social {
    position: absolute;
    left: 701px; top: 47px;
    display: flex; gap: 12px;
  }
  .social span {
    display: block;
    width: 22px; height: 22px;
    border-radius: 50%;
    background: var(--ink);
  }
</style>
</head>
<body>
  <h1 class="poster-title">CORE VALUES</h1>

  <section class="value-card col-1 row-1">
    <div class="notch"></div>
    <div class="badge"><div class="badge-icon" role="img" aria-label="Icon of caring hands holding a heart"></div></div>
    <h2 class="value-name">Be LOYAL</h2>
    <p class="value-text">We take care of our own and provide opportunities to listen and support each other.</p>
  </section>

  <section class="value-card col-2 row-1">
    <div class="notch"></div>
    <div class="badge"><div class="badge-icon" role="img" aria-label="Icon of a lit light bulb"></div></div>
    <h2 class="value-name">Show INITIATIVE</h2>
    <p class="value-text">We celebrate and recognize our own and encourage forward thinking.</p>
  </section>

  <section class="value-card col-3 row-1">
    <div class="notch"></div>
    <div class="badge"><div class="badge-icon" role="img" aria-label="Icon of a handshake"></div></div>
    <h2 class="value-name">Show RESPECT</h2>
    <p class="value-text">We value the diversity and opinions of all.</p>
  </section>

  <section class="value-card col-1 row-2">
    <div class="notch"></div>
    <div class="badge"><div class="badge-icon" role="img" aria-label="Icon of a group of people"></div></div>
    <h2 class="value-name">Think TEAM</h2>
    <p class="value-text">We communicate effectively and work as a team by helping and supporting each other.</p>
  </section>

  <section class="value-card col-2 row-2">
    <div class="notch"></div>
    <div class="badge"><div class="badge-icon" role="img" aria-label="Icon of an open hand over a heart"></div></div>
    <h2 class="value-name">Be OPEN and HONEST</h2>
    <p class="value-text">We are clear and open with each other, and provide an approachable and friendly environment.</p>
  </section>

  <section class="value-card col-3 row-2">
    <div class="notch"></div>
    <div class="badge"><div class="badge-icon" role="img" aria-label="Icon of a smile"></div></div>
    <h2 class="value-name">SMILE</h2>
    <p class="value-text">We are solutions focused and encourage a positive attitude turning a negative into a positive.</p>
  </section>

  <footer class="footer">
    <div class="brand">
      <span class="brand-mark"></span>
      <span class="brand-name">QUORVEL<br>Group</span>
    </div>
    <div class="social" aria-label="Social media links">
      <span></span><span></span><span></span>
    </div>
  </footer>
</body>
</html>
```